Tavenorix - world unique technology for better life - please let them know who am i at first sight

We need a new business card for company which is a provider of unique crystal based technology suitable for all living being. For more information and final design you can use our brochure (our colours are black and blue from brochure).
We use Verdana font

Industry/Entity Type

Business

Contact Information for Business Card

regular dimension

Font styles to use
Other font styles liked:
• Verdana

Requirements
Must have
• Logo
• name
• function/position
• phone
• mobile
• e-mail
• adress
Nice to have
• inovative design (technology directed)

```html
<!DOCTYPE html>
<html lang="en">
<head>
<meta charset="utf-8">
<title>Tavenorix Business Card</title>
<link href="https://fonts.googleapis.com/css2?family=Noto+Sans:wght@400;700&display=swap" rel="stylesheet">
<style>
  :root {
    --stage: #2b2b2d;
    --card-black: #0b0b0c;
    --pattern-dark: #161618;
    --pattern-mid: #232326;
    --brand-blue: #3aa7de;
    --band-light: #4fb6e8;
    --band-deep: #2b8fc7;
    --ink-white: #ffffff;
    --ink-soft: #e6e6e6;
    --font-body: Verdana, "Noto Sans", sans-serif;
  }
  * { margin: 0; padding: 0; box-sizing: border-box; }
  html, body {
    width: 1200px; height: 900px; overflow: hidden;
    background: var(--stage);
    font-family: var(--font-body);
  }
  .sheet {
    width: 1200px; height: 900px;
    display: flex; flex-direction: column;
    align-items: center; justify-content: center; gap: 40px;
  }
  .card {
    position: relative;
    width: 600px; height: 345px;
    background: var(--card-black);
    overflow: hidden;
    box-shadow: 0 10px 30px rgba(0,0,0,.45);
  }

  /* Front face */
  .front-pattern {
    position: absolute; inset: 0;
    background:
      radial-gradient(circle at 45% 48%, var(--pattern-mid) 0%, var(--pattern-dark) 45%, var(--card-black) 80%);
  }
  .front-brand {
    position: absolute; left: 170px; top: 128px;
    display: flex; align-items: center; gap: 14px;
  }
  .brand-dot {
    width: 54px; height: 54px; border-radius: 50%;
    background: var(--brand-blue);
  }
  .brand-name {
    font-size: 36px; font-weight: 400; letter-spacing: 2px;
    color: var(--brand-blue); line-height: 1;
  }
  .front-tagline {
    position: absolute; left: 170px; top: 212px;
    font-size: 12.5px; color: var(--brand-blue);
  }
  .front-url {
    position: absolute; left: 170px; top: 236px;
    font-size: 14px; font-weight: 700; color: var(--ink-white);
  }

  /* Back face */
  .band {
    position: absolute; left: 0; top: 0;
    width: 600px; height: 160px;
    background: linear-gradient(100deg, var(--band-light) 0%, var(--brand-blue) 55%, var(--band-deep) 100%);
  }
  .band-notch {
    position: absolute; left: 70px; top: 159px;
    width: 0; height: 0;
    border-left: 12px solid var(--brand-blue);
    border-right: 12px solid transparent;
    border-top: 14px solid var(--brand-blue);
  }
  .back-brand {
    position: absolute; left: 26px; top: 52px;
    display: flex; align-items: center; gap: 12px;
  }
  .back-brand .brand-dot { width: 46px; height: 46px; background: var(--ink-white); }
  .back-brand .brand-name { font-size: 30px; color: var(--ink-white); }
  .social-row {
    position: absolute; right: 36px; top: 110px;
    display: flex; gap: 9px;
  }
  .social-dot {
    width: 18px; height: 18px; border-radius: 50%;
    background: rgba(255,255,255,.28);
  }
  .person {
    position: absolute; left: 26px; top: 194px;
  }
  .person-name {
    font-size: 24px; font-weight: 700; color: var(--brand-blue);
    letter-spacing: .5px;
  }
  .person-role {
    font-size: 12px; color: var(--ink-soft); margin-top: 4px;
  }
  .contact-lines {
    font-size: 12px; color: var(--ink-soft); line-height: 1.45;
  }
  .contact-lines b { color: var(--brand-blue); font-weight: 700; margin-right: 6px; }
  .person .contact-lines { margin-top: 28px; }
  .company {
    position: absolute; left: 330px; top: 176px;
  }
  .company-name {
    font-size: 12.5px; font-weight: 700; color: var(--brand-blue);
  }
  .company-address {
    font-size: 12px; color: var(--ink-soft); line-height: 1.45; margin-top: 2px;
  }
  .company .contact-lines { margin-top: 20px; }
</style>
</head>
<body>
<main class="sheet">

  <section class="card card-front">
    <div class="front-pattern" role="img" aria-label="Dark interlaced crystal-line decorative pattern"></div>
    <div class="front-brand">
      <span class="brand-dot"></span>
      <span class="brand-name">TAVENORIX</span>
    </div>
    <p class="front-tagline">Clear living energy shaped by nature and careful science</p>
    <p class="front-url">www.tavenorix.co.uk</p>
  </section>

  <section class="card card-back">
    <div class="band" role="img" aria-label="Blue-toned technology imagery band"></div>
    <span class="band-notch"></span>
    <div class="back-brand">
      <span class="brand-dot"></span>
      <span class="brand-name">TAVENORIX</span>
    </div>
    <div class="social-row" aria-label="Social links">
      <span class="social-dot"></span>
      <span class="social-dot"></span>
      <span class="social-dot"></span>
      <span class="social-dot"></span>
    </div>

    <div class="person">
      <h1 class="person-name">MARTA LINDE</h1>
      <p class="person-role">Function/Position</p>
      <p class="contact-lines">
        <b>M</b>+ 0 555 210 4839<br>
        <b>E</b>marta@tavenorix.eu
      </p>
    </div>

    <div class="company">
      <p class="company-name">TAVENORIX International Ltd</p>
      <p class="company-address">28-32 Harlow Row<br>London EC2R 7QN, United Kingdom</p>
      <p class="contact-lines">
        <b>T</b>+ 44 (0) 20 555 0187<br>
        <b>E</b>info@tavenorix.eu
      </p>
    </div>
  </section>

</main>
</body>
</html>
```